Corvantis websites redesign

Www.cor-vantis.com needs to be redesigned along with updations. The incremental material will be provided for the updations. We are looking for complete redesign of the pages with the new content. The complete write up will be provided soon

Target Market(s)

Global

Coding

Coded - Design and coding required

Number of Pages Required

5+ page

Requirements
Must have
• A clean and slick design for the Consulting.
Should not have
• Too many pictures which reduces the speed of the site

```html
<!DOCTYPE html>
<html lang="en">
<head>
<meta charset="utf-8">
<title>Corvantis — About Us</title>
<link href="https://fonts.googleapis.com/css2?family=Jost:wght@300;400;500&display=swap" rel="stylesheet">
<style>
  :root {
    --brand-navy: #2c3e57;
    --nav-maroon: #6e1f22;
    --nav-active: #1f7aa0;
    --hero-deep: #1d2f40;
    --hero-mid: #4a6478;
    --hero-light: #8fa6b6;
    --footer-bg: #0d1e2a;
    --white: #ffffff;
    --footer-text: #c9d2d8;
  }
  * { box-sizing: border-box; margin: 0; padding: 0; }
  html, body { width: 1200px; height: 894px; overflow: hidden; background: var(--white); }
  body { font-family: 'Jost', sans-serif; }

  .site-header {
    height: 132px;
    display: flex;
    align-items: center;
    justify-content: space-between;
    padding: 0 80px 0 84px;
    background: var(--white);
  }
  .brand {
    display: flex;
    align-items: center;
    gap: 14px;
    font-size: 38px;
    font-weight: 400;
    color: var(--brand-navy);
    letter-spacing: 0.2px;
  }
  .brand-dot {
    width: 40px; height: 40px;
    border-radius: 50%;
    background: var(--brand-navy);
  }
  .main-nav { display: flex; gap: 27px; }
  .main-nav a {
    font-size: 17px;
    font-weight: 500;
    letter-spacing: 0.4px;
    color: var(--nav-maroon);
    text-decoration: none;
    text-transform: uppercase;
  }
  .main-nav a.is-active { color: var(--nav-active); }

  .hero {
    position: relative;
    height: 702px;
    overflow: hidden;
  }
  .hero-photo {
    position: absolute; inset: 0;
    background:
      radial-gradient(ellipse 55% 60% at 78% 55%, rgba(160,180,195,0.55), transparent 70%),
      radial-gradient(ellipse 35% 30% at 35% 45%, rgba(150,160,170,0.45), transparent 70%),
      linear-gradient(180deg, var(--hero-mid) 0%, var(--hero-deep) 65%, var(--hero-light) 100%);
  }
  .hero-content {
    position: relative;
    padding: 92px 0 0 84px;
    width: 680px;
    color: var(--white);
  }
  .hero-title {
    font-size: 40px;
    font-weight: 300;
    letter-spacing: 0.5px;
    margin-bottom: 86px;
  }
  .hero-content p {
    font-size: 13.5px;
    font-weight: 300;
    line-height: 19px;
    margin-bottom: 36px;
  }
  .hero-content p.tight { margin-bottom: 16px; }

  .site-footer {
    height: 60px;
    background: var(--footer-bg);
    display: flex;
    align-items: center;
    justify-content: flex-end;
    padding-right: 82px;
  }
  .site-footer small {
    font-size: 11px;
    font-weight: 500;
    color: var(--footer-text);
    letter-spacing: 0.2px;
  }
</style>
</head>
<body>
  <header class="site-header">
    <div class="brand"><span class="brand-dot"></span>Corvantis</div>
    <nav class="main-nav">
      <a href="#" class="is-active">Home</a>
      <a href="#">Founder</a>
      <a href="#">Consultancy</a>
      <a href="#">System</a>
      <a href="#">Case Studies</a>
      <a href="#">Contact</a>
    </nav>
  </header>

  <main class="hero">
    <div class="hero-photo" role="img" aria-label="Photo of business people shaking hands over a desk with charts and a tablet, in blue-grey tones"></div>
    <section class="hero-content">
      <h1 class="hero-title">ABOUT US</h1>
      <p>Corvantis Consultancy Limited capitalizes on synergies arising from trade and investment linkages between countries and knowledge of traditional and non-traditional pools of liquidity to provide consultancy services to Emerging country banks, Corporates and SMEs.</p>
      <p>The Consultancy provides bank neutral views to Corporates and SMEs in Asian emerging markets and helps in improving financial structure and efficient use of funds. Our endeavor is to provide a distinct bottom line advantage to our clients. The primary focus is in regionalisation of the banking relationship across the globe, providing structured finance solutions and off balance sheet solutions.</p>
      <p class="tight">The consultancy for the Banks and Non Banking Financial Institutions is focused on risk mitigation techniques, Export Credit Agency business and trade origination and distribution strategies along with raising long term liabilities.</p>
      <p>We invest actively in developing technology platform for better distribution, disintermediation, efficient process flow and cost effective delivery of solutions.</p>
    </section>
  </main>

  <footer class="site-footer">
    <small>© CORVANTIS CONSULTANCY LIMITED</small>
  </footer>
</body>
</html>
```